Consulting Company needs business card design

We need a business card design for a new consulting and business solutions company based in Bermuda called Corvale Partners Limited. Looking for a double sided business card with one side only including the company logo thats attached and the other including contact information. Logo contains blue and turquoise colors and is fine to be on both sides of the card.
Contact Information for Business Card
Corvale Partners Limited
P.O. Box HM318
Devonshire DV BX
Bermuda
Name: Marcus Pellegrin
Position: Director
Telephone: 1 441 733 4906
Email: mpellegrin@corvale.example
Website: www.corvale.example

```html
<!DOCTYPE html>
<html lang="en">
<head>
<meta charset="utf-8">
<title>Corvale Partners Limited — Business Card</title>
<link rel="stylesheet" href="https://fonts.googleapis.com/css2?family=Open+Sans:wght@400;600;700&display=swap">
<style>
  :root {
    --stage: #2a2d31;
    --card-white: #ffffff;
    --card-dark: #2f3135;
    --ink: #2b2b2b;
    --brand-blue: #229fdf;
    --brand-teal: #15b7c2;
    --card-w: 600px;
    --card-h: 343px;
  }
  * { box-sizing: border-box; margin: 0; padding: 0; }
  html, body {
    width: 1200px; height: 900px; overflow: hidden;
    background: var(--stage);
    font-family: "Open Sans", Arial, sans-serif;
  }
  .stage {
    position: relative; width: 1200px; height: 900px;
    display: flex; flex-direction: column; align-items: center; justify-content: center; gap: 60px;
  }
  .card {
    position: relative; width: var(--card-w); height: var(--card-h);
    border-radius: 26px; overflow: hidden;
    box-shadow: 0 14px 30px rgba(0,0,0,.35);
  }

  /* Front: contact side */
  .card-front { background: var(--card-white); color: var(--ink); }
  .front-mark {
    position: absolute; left: 56px; top: 44px;
    width: 120px; height: 120px; border-radius: 50%;
    background: var(--brand-blue);
  }
  .person { position: absolute; left: 318px; top: 118px; }
  .person-name {
    font-weight: 700; font-size: 22px; letter-spacing: .5px; line-height: 1.1;
    text-transform: uppercase;
  }
  .person-name .surname { color: var(--brand-blue); }
  .person-role { font-size: 19px; font-weight: 400; line-height: 1.2; }
  .contact-list { list-style: none; margin-top: 16px; }
  .contact-list li {
    display: flex; align-items: center; gap: 9px;
    font-size: 14.5px; line-height: 23px;
  }
  .contact-list svg { width: 13px; height: 13px; fill: var(--brand-blue); flex: none; }
  .address-line {
    position: absolute; left: 34px; bottom: 30px;
    font-size: 14px; display: flex; gap: 26px;
  }
  .address-line .company { font-weight: 600; }
  .corner-tab {
    position: absolute; right: 0; bottom: 0;
    width: 24px; height: 26px; background: var(--brand-blue);
  }

  /* Back: logo side */
  .card-back { background: var(--card-dark); }
  .back-band {
    position: absolute; left: 0; right: 0; bottom: 0; height: 74px;
    background: var(--brand-teal);
  }
  .back-logo {
    position: absolute; left: 0; right: 0; top: 78px;
    display: flex; align-items: center; justify-content: center; gap: 18px;
  }
  .back-mark { width: 64px; height: 64px; border-radius: 50%; background: var(--brand-blue); flex: none; }
  .back-name {
    color: var(--brand-blue); font-weight: 600; font-size: 30px;
    letter-spacing: 2px; text-transform: uppercase; line-height: 1.15;
  }
</style>
</head>
<body>
<main class="stage">

  <section class="card card-front" aria-label="Business card, contact side">
    <div class="front-mark"></div>

    <div class="person">
      <p class="person-name">Marcus <span class="surname">Pellegrin</span></p>
      <p class="person-role">Director</p>
      <ul class="contact-list">
        <li>
          <svg viewBox="0 0 24 24" aria-hidden="true"><path d="M6.6 10.8a15.1 15.1 0 0 0 6.6 6.6l2.2-2.2c.3-.3.7-.4 1-.2 1.1.4 2.3.6 3.6.6.6 0 1 .4 1 1V20c0 .6-.4 1-1 1A17 17 0 0 1 3 4c0-.6.4-1 1-1h3.5c.6 0 1 .4 1 1 0 1.3.2 2.5.6 3.6.1.3 0 .7-.2 1z"/></svg>
          <span>1 441 733 4906</span>
        </li>
        <li>
          <svg viewBox="0 0 24 24" aria-hidden="true"><path d="M2 5h20v14H2z M3.5 6.5 12 13l8.5-6.5" fill="none" stroke="#229fdf" stroke-width="0"/><path d="M2 5h20v2l-10 7L2 7z"/><path d="M2 9l10 7 10-7v10H2z"/></svg>
          <span>mpellegrin@corvale.example</span>
        </li>
        <li>
          <svg viewBox="0 0 24 24" aria-hidden="true"><circle cx="12" cy="12" r="10" fill="none" stroke="#229fdf" stroke-width="2.4"/><path d="M2 12h20M12 2c3 3 3 17 0 20M12 2c-3 3-3 17 0 20" fill="none" stroke="#229fdf" stroke-width="2"/></svg>
          <span>www.corvale.example</span>
        </li>
      </ul>
    </div>

    <p class="address-line">
      <span class="company">Corvale Partners Limited</span>
      <span>P.O. Box HM318, Devonshire DV BX, Bermuda</span>
    </p>
    <div class="corner-tab"></div>
  </section>

  <section class="card card-back" aria-label="Business card, logo side">
    <div class="back-logo">
      <div class="back-mark"></div>
      <p class="back-name">Corvale<br>Partners Limited</p>
    </div>
    <div class="back-band"></div>
  </section>

</main>
</body>
</html>
```